Business card design needed

The company name is Wendale Architects. We are an architectural company based in Melbourne,Australia that has a mix of client base from health care, commercial office, aged care, multi-residential, single residential and retail. Design type is contemporary.

Suggest the base colours need to be black and white. Please leave an area on the back of the card available for handwritten notes.

Target Market(s)

Generally corporate, aged 30 to 65

Industry/Entity Type

Residential

Contact Information for Business Card

Wendale Architects
Mark Wendale
14 Pellow Street
Rosevale VIC 3071
T (03) 9512 4067
M 0438 617 295
E mw@wendalearc.com.au

Logo Text

WA

Logo styles of interest
Emblem Logo
Abstract Logo
Lettermark Logo
Requirements
Must have
• I am having trouble attaching a sketch so would really appreciate your effort to try the following brief.

Black and White (B&W)
Would like different card cutout profile. Logo Example, use the half circle curve of the G to form the left edge of the card with no margin. The A is to sit inside the G, connected to the G by its horizontal. The A has its cross bar and lower right leg removed. Card in black, text in white.

Back of card to be black text on white background with services provided.

Client Focused Service
Architecture and Design
Functional Planning
Town Planning
Feasability Studies
Contract Documentation
Contract Administration
Project Management

Simple elegant text, Ariel or similar
Nice to have
• Integrated logo and card cut-out.

Card base black on front, white on back
Should not have
• Too many colours
Fussy details

```html
<!DOCTYPE html>
<html lang="en">
<head>
<meta charset="utf-8">
<title>Wendale Architects – Business Card</title>
<link rel="stylesheet" href="https://fonts.googleapis.com/css2?family=Arimo:wght@400;700&display=swap">
<style>
  :root {
    --backdrop: #939598;
    --card-dark: #3a393d;
    --card-light: #ffffff;
    --ink-light: #ffffff;
    --ink-dark: #231f20;
    --monogram-faint: #e4e4e5;
    --divider: #b5b5b7;
  }
  * { margin: 0; padding: 0; box-sizing: border-box; }
  html, body {
    width: 1200px; height: 628px; overflow: hidden;
    background: var(--backdrop);
    font-family: "Arimo", Arial, sans-serif;
  }
  .canvas { position: relative; width: 1200px; height: 628px; }
  .card-shapes { position: absolute; inset: 0; }
  .card-front-shape { fill: var(--card-dark); }
  .card-back-shape { fill: var(--card-light); }

  .front-monogram {
    position: absolute; left: 112px; top: 236px; width: 256px;
    text-align: center; color: var(--ink-light);
    font-weight: 700; font-size: 140px; line-height: 1; letter-spacing: -4px;
  }
  .company-name {
    position: absolute; left: 385px; top: 214px;
    color: var(--ink-light); font-weight: 700; font-size: 18px;
    text-decoration: underline; text-underline-offset: 5px; text-decoration-thickness: 2px;
    letter-spacing: 0.2px; white-space: nowrap;
  }
  .contact-lines {
    position: absolute; right: 602px; top: 358px;
    color: var(--ink-light); font-size: 14px; line-height: 18px; text-align: right;
    white-space: nowrap;
  }
  .address {
    position: absolute; left: 387px; top: 421px;
    color: var(--ink-light); font-size: 14px; line-height: 18px;
    white-space: nowrap;
  }

  .back-monogram {
    position: absolute; left: 808px; top: 255px; width: 140px;
    text-align: center; color: var(--monogram-faint);
    font-weight: 700; font-size: 66px; line-height: 1; letter-spacing: -2px;
  }
  .services {
    position: absolute; left: 728px; top: 502px; width: 300px;
    text-align: center; color: var(--ink-dark); font-size: 10.5px; line-height: 15px;
    list-style: none; white-space: nowrap;
  }
  .services .sep { color: var(--divider); padding: 0 2px; }
</style>
</head>
<body>
<main class="canvas">
  <svg class="card-shapes" width="1200" height="628" viewBox="0 0 1200 628" aria-hidden="true">
    <path class="card-front-shape" d="M247 170 H621 V470 H247 A150 150 0 0 1 247 170 Z"/>
    <path class="card-back-shape" d="M728 568 V165 A150 90 0 0 1 1028 165 V568 Z"/>
  </svg>

  <section class="card-front" aria-label="Card front">
    <div class="front-monogram">WA</div>
    <h1 class="company-name">WENDALE ARCHITECTS</h1>
    <p class="contact-lines">
      T (03) 9512 4067<br>
      M 0438 617 295<br>
      E mw@wendalearc.com.au
    </p>
    <p class="address">
      Wendale Architects Mark Wendale<br>
      14 Pellow Street Rosevale VIC 3071
    </p>
  </section>

  <section class="card-back" aria-label="Card back">
    <div class="back-monogram">WA</div>
    <ul class="services">
      <li>Client Focused Service</li>
      <li>Architecture and Design<span class="sep">|</span>Contract Administration</li>
      <li>Project Management<span class="sep">|</span>Town Planning<span class="sep">|</span>Feasability Studies</li>
      <li>Contract Documentation<span class="sep">|</span>Functional Planning</li>
    </ul>
  </section>
</main>
</body>
</html>
```